Dapple Brew, a new venture, serving our customers at functions and events, lovingly made coffee fro

www.dapplebrew.com.au

Dapple Brew Wordpress

The font type of our logo is: La Chatte à Maman (it can be downloaded in dafont.com)

Our trading name is Dapple Brew. We have a passion for well made coffee and providing service with affection.

Our new logo design is being placed on the side and rear of our restored 1976 camper van. I have attached our logo and a picture of our van. We would like to own the rights to all work on our site, with access to make additions and amendments as required with no restrictions.

We want our event business to grow through our branding of great service and lovingly made coffee.

We would like our WordPress design to be simple with a retro image that our 76 camper van portrays as well as the hipster coffee culture of Melbourne.

To begin with we are thinking of 5 pages but are open to any suggestions you think would benefit our development. We would also like to have links to our new Social and Photo pages on the bottom of each page.

Logo -Like us on Social
https://www.facebook.com/pages/Dapple-Brew/5820371946618405

Logo -follow us on Photo
Dapple_brew

Home

Beautifully made coffee is a pleasure we should all enjoy at least once in our day.
Served from our restored 1976 camper van we strive to provide you with an experience that will enhance your day. The care we show comes from years of training and experience as a Battista in several countries around the world.
We trust the joy of our lovingly made coffee and our retro style service will linger.
Serving great coffee at an event or function near you
Dapple Brew.

About
Dapple brew believes in good old fashion retro service and a high a quality product. We care that our customers receive a beautifully made coffee, chai or hot chocolate. We serve our patrons with a heartfelt smile, aiming to enhance their day.
We are fortunate enough to operate from our recently restored 1976 camper van at functions and events around Melbourne.
You can follow us on Social and Photo or book us for you special function via our contact page.
We look forward to wing able to serve you.
Dapple Brew.

Contact Us - Safe and secure

To book us at your special function, please fill in your details below and we will respond to your query as soon as possible.

Name:

Company name:

Phone number:

Email address:

Question or comment: ( box )

Dapple Brew
Melbourne, Victoria, Australia
Info@dapplebrew.com.au
0471 925 164
Operating at your local function or event

Blog
Social and Photo integration.

Links

We have a heartfelt passionate and eternal pursuit for exceeding expectations, providing a memorable experience. It follows that we align ourselves with organizations, business's and people who also strive for perfection in what they do, providing great services, products and customer care.

Feel free to contact some of our contacts below who we have found to be above and beyond.

The Tamper Mill group - equipment suppliers

http://www.grindworks-supply.com.au

Kesi- barista consulting services

https://www.facebook.com/pages/Prime...Kesi/7301958264417086

Reedfinch Swimming Club

http://reedfinch.com.au/

Wexmoor Baseball Club

www.wexmoorfalcons.com.au/

Pellby Autos

http://www.pellbyautos.com.au

Target Market(s)

Lovers of Coffee at events and functions. Customers wanting coffee catered for at their event of function

Industry/Entity Type

Cafe

Font styles to use
Other font styles liked:
• La Chatte à Maman

Requirements
Must have
• Our logo design
• 5 pages but are open to any suggestions you think would benefit our development. We would also like to have links to our new Social and Photo pages on the bottom of each page.
Nice to have
• Your artistic flair and input

```html
<!DOCTYPE html>
<html lang="en">
<head>
<meta charset="utf-8">
<title>Dapple Brew — Lovingly Made Coffee</title>
<link href="https://fonts.googleapis.com/css2?family=Raleway:wght@400;500;600;700&family=Kaushan+Script&display=swap" rel="stylesheet">
<style>
:root{
  --espresso:#2a1a12;
  --roast:#3b271c;
  --mocha:#5a3a2a;
  --crema:#c8a07a;
  --cream:#f5f1ec;
  --paper:#ffffff;
  --mist:#ececec;
  --ink:#3a3330;
  --muted:#8a817b;
  --night:#1c1715;
  --char:#141110;
  --accent:#6b4430;
}
*{box-sizing:border-box;margin:0;padding:0}
html,body{width:1200px;height:2532px;overflow:hidden}
body{font-family:"Raleway",Arial,sans-serif;color:var(--ink);background:var(--paper);position:relative}
.script{font-family:"Kaushan Script",cursive}

/* hero */
.hero{position:absolute;left:0;top:0;width:1200px;height:620px;overflow:hidden}
.hero-photo{position:absolute;inset:0;background:radial-gradient(ellipse at 25% 30%,#6b4532 0%,#3e2619 40%,#221410 80%),#2a1a12}
.hero-shade{position:absolute;inset:0;background:linear-gradient(180deg,rgba(0,0,0,.15),rgba(0,0,0,.35))}
.topbar{position:absolute;top:0;left:0;right:0;height:118px}
.brand{position:absolute;left:130px;top:14px;width:140px;height:140px;border-radius:50%;background:var(--char);border:3px solid var(--paper);display:flex;align-items:center;justify-content:center;text-align:center;color:var(--paper);font-weight:700;font-size:22px;line-height:1.1;z-index:3}
.search{position:absolute;left:800px;top:22px;width:200px;height:30px;background:var(--paper);border-radius:2px;font-size:13px;color:var(--muted);padding:7px 10px}
.search svg{position:absolute;right:8px;top:8px}
.social{position:absolute;top:20px;left:1016px;display:flex;gap:12px}
.social span{width:34px;height:34px;border-radius:50%;background:rgba(255,255,255,.9)}
.nav{position:absolute;left:660px;top:86px;height:36px;display:flex;background:var(--char)}
.nav a{color:var(--paper);text-decoration:none;font-size:12px;font-weight:700;letter-spacing:1px;padding:12px 20px}
.nav a.active{background:var(--mocha)}
.hero-mark{position:absolute;left:572px;top:250px}
.hero-title{position:absolute;top:380px;left:0;right:0;text-align:center;color:var(--paper);font-size:46px;font-weight:600;letter-spacing:.5px}
.hero-sub{position:absolute;top:442px;left:300px;width:600px;text-align:center;color:#e8ddd4;font-size:14px;line-height:1.6}
.hero-wave{position:absolute;left:0;bottom:0}

/* welcome */
.welcome{position:absolute;top:620px;left:0;width:1200px;height:300px;text-align:center}
.section-title{font-size:40px;font-weight:500;color:var(--ink)}
.section-title .script{font-size:40px}
.divider{display:block;margin:10px auto 16px}
.welcome p{width:860px;margin:0 auto 8px;font-size:14px;line-height:1.7;color:var(--muted)}
.welcome .tagline{font-family:"Kaushan Script",cursive;font-size:24px;line-height:1.3;color:var(--mocha);margin-top:14px}

/* booking */
.booking{position:absolute;top:920px;left:0;width:1200px;height:240px;background:var(--mist);text-align:center;padding-top:36px}
.booking .hours{font-size:13px;color:var(--muted);margin-top:-4px}
.book-form{display:flex;gap:18px;justify-content:center;margin-top:28px}
.field{width:220px;height:40px;background:var(--paper);border:1px solid #d6d2ce;font-size:13px;color:var(--muted);text-align:left;padding:12px 14px;position:relative}
.field.short{width:200px}
.field svg{position:absolute;right:12px;top:16px}
.book-btn{width:190px;height:40px;background:var(--roast);color:var(--paper);font-size:12px;font-weight:700;letter-spacing:1px;padding-top:13px}

/* events */
.events{position:absolute;top:1160px;left:0;width:1200px;height:500px;background:linear-gradient(180deg,#26201d,#151211);color:var(--paper);text-align:center;padding-top:40px}
.events .section-title{color:var(--paper)}
.event-photo{position:absolute;left:140px;top:160px;width:410px;height:260px;background:linear-gradient(135deg,#8a5a3a,#3a2418 60%,#1e140f)}
.event-card{position:absolute;left:540px;top:178px;width:520px;height:230px;background:rgba(90,58,42,.92);text-align:left;padding:22px 26px}
.event-card h3{font-size:19px;font-weight:600;margin-bottom:12px}
.event-card p{font-size:13px;line-height:1.6;color:#e6d7cb}
.event-card .when{margin-top:12px;font-size:12px;color:var(--crema)}
.event-card .more{margin-top:16px;font-size:12px;font-weight:700;letter-spacing:1px}
.dots{position:absolute;left:0;right:0;top:452px;display:flex;gap:10px;justify-content:center}
.dots span{width:11px;height:11px;border-radius:50%;background:#777}
.dots span.on{background:var(--paper)}

/* feeds */
.feeds{position:absolute;top:1660px;left:0;width:1200px;height:380px;background:var(--paper);display:flex;gap:40px;justify-content:center;padding-top:48px}
.feed{width:310px;height:290px;border:1px solid #e2dedb;padding:14px;text-align:center}
.feed h4{font-size:20px;font-weight:500;margin-bottom:12px}
.feed h4 .script{font-size:20px}
.feed-photo{height:150px;background:linear-gradient(135deg,#e9e0d7,#9c7458 60%,#5a3a2a)}
.feed-caption{text-align:left;margin-top:10px;font-size:13px;font-weight:600;color:var(--ink)}
.feed-meta{text-align:left;font-size:11px;color:var(--muted);margin-top:4px}
.page-box{margin-top:10px;text-align:left;font-size:11px;color:var(--muted)}
.page-box .row{display:flex;gap:4px;margin-top:6px}
.page-box .row span{width:22px;height:22px;background:#d9d3ce}
.like-btn{display:inline-block;margin-top:8px;border:1px solid #ccc;padding:3px 8px;font-size:11px;color:var(--ink)}

/* newsletter */
.newsletter{position:absolute;top:2052px;left:0;width:1200px;height:58px;background:var(--mocha);display:flex;align-items:center;justify-content:center;gap:14px;color:var(--paper);font-size:15px;font-weight:600}
.newsletter .input{width:320px;height:32px;background:var(--paper);color:var(--muted);font-size:12px;font-weight:400;padding:9px 12px}
.newsletter .go{width:80px;height:32px;background:var(--roast);font-size:12px;letter-spacing:1px;text-align:center;padding-top:9px}

/* footer */
.footer{position:absolute;top:2110px;left:0;width:1200px;height:422px;background:radial-gradient(ellipse at 50% 40%,#2a2522,#141110);text-align:center;color:#d8d0ca}
.footer .brand{position:absolute;left:540px;top:48px;width:120px;height:120px;font-size:19px;border-color:#888}
.footer address{position:absolute;top:210px;left:0;right:0;font-style:normal;font-size:15px;line-height:2}
.copyright{position:absolute;bottom:0;left:0;right:0;height:58px;border-top:1px solid #2e2825;font-size:12px;color:var(--muted);padding-top:22px}
</style>
</head>
<body>

<header class="hero">
  <div class="hero-photo" role="img" aria-label="Close-up of dark roasted coffee beans"></div>
  <div class="hero-shade"></div>
  <div class="topbar">
    <div class="brand">Dapple<br>Brew</div>
    <div class="search">Search
      <svg width="14" height="14" viewBox="0 0 14 14"><circle cx="6" cy="6" r="4.5" fill="none" stroke="#888" stroke-width="1.6"/><line x1="9.5" y1="9.5" x2="13" y2="13" stroke="#888" stroke-width="1.6"/></svg>
    </div>
    <div class="social"><span></span><span></span></div>
    <nav class="nav">
      <a class="active">HOME</a><a>ABOUT</a><a>BLOG</a><a>LINKS</a><a>CONTACT</a>
    </nav>
  </div>
  <svg class="hero-mark" width="56" height="76" viewBox="0 0 56 76">
    <ellipse cx="28" cy="38" rx="25" ry="35" fill="#f5f1ec"/>
    <path d="M28 5 C16 25 40 50 28 71" fill="none" stroke="#3b271c" stroke-width="4"/>
  </svg>
  <h1 class="hero-title">We Have A Passion For Well Made Coffee</h1>
  <p class="hero-sub">Dapple Brew, a new venture, serving our customers at functions and events, lovingly made coffee from our restored 1976 camper van.</p>
  <svg class="hero-wave" width="1200" height="40" viewBox="0 0 1200 40" preserveAspectRatio="none">
    <path d="M0 40 L0 22 Q30 6 60 22 T120 22 T180 22 T240 22 T300 22 T360 22 T420 22 T480 22 T540 22 T600 22 T660 22 T720 22 T780 22 T840 22 T900 22 T960 22 T1020 22 T1080 22 T1140 22 T1200 22 L1200 40 Z" fill="#ffffff"/>
  </svg>
</header>

<section class="welcome">
  <h2 class="section-title" style="margin-top:18px">Welcome <span class="script">Dapple Brew</span></h2>
  <svg class="divider" width="120" height="12" viewBox="0 0 120 12"><line x1="0" y1="6" x2="50" y2="6" stroke="#8a817b"/><circle cx="60" cy="6" r="4" fill="#5a3a2a"/><line x1="70" y1="6" x2="120" y2="6" stroke="#8a817b"/></svg>
  <p>Beautifully made coffee is a pleasure we should all enjoy at least once in our day.</p>
  <p>Served from our restored 1976 camper van we strive to provide you with an experience that will enhance your day. The care we show comes from years of training and experience as a Barista in several countries around the world.</p>
  <p>We trust the joy of our lovingly made coffee and our retro style service will linger.</p>
  <p class="tagline">Serving Great Coffee at an Event or Function Near You</p>
</section>

<section class="booking">
  <h2 class="section-title">Book a <span class="script">Table</span></h2>
  <svg class="divider" width="120" height="12" viewBox="0 0 120 12"><line x1="0" y1="6" x2="50" y2="6" stroke="#8a817b"/><circle cx="60" cy="6" r="4" fill="#5a3a2a"/><line x1="70" y1="6" x2="120" y2="6" stroke="#8a817b"/></svg>
  <p class="hours">Opening hours 9am - 5pm, call ahead to reserve</p>
  <div class="book-form">
    <div class="field">Name</div>
    <div class="field">Date</div>
    <div class="field short">Persons<svg width="10" height="6" viewBox="0 0 10 6"><path d="M0 0 L5 6 L10 0Z" fill="#888"/></svg></div>
    <div class="book-btn">BOOK A TABLE</div>
  </div>
</section>

<section class="events">
  <h2 class="section-title">Upcoming <span class="script">Events</span></h2>
  <svg class="divider" width="120" height="12" viewBox="0 0 120 12"><line x1="0" y1="6" x2="50" y2="6" stroke="#999"/><circle cx="60" cy="6" r="4" fill="#c8a07a"/><line x1="70" y1="6" x2="120" y2="6" stroke="#999"/></svg>
  <div class="event-photo" role="img" aria-label="Busy coffee bar with espresso machine at an event"></div>
  <article class="event-card">
    <h3>We trust the joy of our lovingly made coffee</h3>
    <p>Served from our restored 1976 camper van we strive to provide you with an experience that will enhance your day. The care we show comes from years of training and experience as a Barista in several countries around the world.</p>
    <p class="when">12.00 PM Monday, 13 Aug</p>
    <p class="more">VIEW DETAILS</p>
  </article>
  <div class="dots"><span class="on"></span><span></span><span></span></div>
</section>

<section class="feeds">
  <div class="feed">
    <h4>From <span class="script">Blog</span></h4>
    <div class="feed-photo" role="img" aria-label="Cup of latte with foam art"></div>
    <p class="feed-caption">We Trust The Joy Of Our</p>
    <p class="feed-meta">Posted by Admin</p>
  </div>
  <div class="feed">
    <h4>Social <span class="script">Feed</span></h4>
    <div class="feed-photo" role="img" aria-label="Coffee cup photo from the page cover"></div>
    <div class="page-box">Be the first of your friends to like this
      <div class="row"><span></span><span></span><span></span><span></span><span></span><span></span><span></span></div>
      <span class="like-btn">Like Page</span>
    </div>
  </div>
  <div class="feed">
    <h4>Photo <span class="script">Feed</span></h4>
    <div class="feed-photo" role="img" aria-label="Latest coffee photo posted to the feed"></div>
    <div class="page-box">Be the first of your friends to like this
      <div class="row"><span></span><span></span><span></span><span></span><span></span><span></span><span></span></div>
      <span class="like-btn">Follow</span>
    </div>
  </div>
</section>

<section class="newsletter">
  <span>Get Our Newsletter</span>
  <div class="input">Enter Email Here</div>
  <div class="go">SIGN IN</div>
</section>

<footer class="footer">
  <div class="brand">Dapple<br>Brew</div>
  <address>
    Melbourne, Victoria, Australia<br>
    Call: 0471 925 164<br>
    Email: Info@dapplebrew.com.au
  </address>
  <div class="copyright">© All Rights Reserved. Dapple Brew. Website Design.</div>
</footer>

</body>
</html>
```